Templates for Construction Company

We are looking to have templates prepared for all aspects of our letter sending. Using our brand design. with similar layouts that look the same.

Letterheads design & Email signatures

We use letter heads for - quotes, contract correspondence, variations, formal letters, invitations

Target Market(s)

Clients documents sent in emails

Industry/Entity Type

Construction

Font styles to use
Serif
Sans Serif

Colors
0054AA
0677BA
7BADD7
CADEEF
E8F1F8

Requirements
Must have
• Easy to read, water marks on page
Nice to have
• Different options for different letters

```html
<!DOCTYPE html>
<html lang="en">
<head>
<meta charset="utf-8">
<title>Framewell Group – Stationery</title>
<link href="https://fonts.googleapis.com/css2?family=Montserrat:wght@700&family=Open+Sans:wght@400;600&display=swap" rel="stylesheet">
<style>
  :root {
    --backdrop: #dcdde0;
    --paper: #f2f2f4;
    --brand-blue: #5b8fd0;
    --mark-grey: #8a8a8c;
    --text-grey: #5a5a5c;
    --text-soft: #77787a;
  }
  * { margin: 0; padding: 0; box-sizing: border-box; }
  html, body {
    width: 875px; height: 1200px; overflow: hidden;
    background: var(--backdrop);
    font-family: "Open Sans", Arial, sans-serif;
    color: var(--text-grey);
  }
  .sheet {
    position: absolute; left: 127px; width: 636px;
    background: var(--paper);
    box-shadow: 0 2px 8px rgba(0,0,0,0.15);
  }
  .business-card { top: 52px; height: 231px; }
  .letterhead { top: 325px; height: 831px; }
  .wordmark {
    position: absolute; display: flex; align-items: center; gap: 8px;
    font-family: "Montserrat", Arial, sans-serif; font-weight: 700;
    font-size: 28px; color: var(--brand-blue); letter-spacing: -0.5px;
  }
  .wordmark-square { width: 14px; height: 14px; background: var(--mark-grey); }
  .business-card .wordmark { left: 49px; top: 92px; }
  .letterhead .wordmark { left: 41px; top: 66px; }

  .holder-name { position: absolute; left: 391px; top: 31px; font-size: 15px; color: var(--brand-blue); }
  .holder-role { position: absolute; left: 392px; top: 50px; font-size: 7px; color: var(--text-soft); }
  .accent-rule { position: absolute; width: 2px; background: var(--brand-blue); }
  .business-card .accent-rule { left: 392px; top: 63px; height: 55px; }
  .letterhead .accent-rule { left: 64px; top: 234px; height: 414px; width: 1.5px; }
  .postal-address { position: absolute; left: 391px; top: 124px; font-size: 8.5px; line-height: 12.5px; color: var(--text-soft); }

  .contact-list { position: absolute; list-style: none; font-size: 8.5px; color: var(--text-soft); }
  .contact-list li { display: flex; align-items: center; gap: 7px; height: 12.5px; }
  .contact-list svg { width: 7px; height: 7px; fill: var(--brand-blue); }
  .business-card .contact-list { left: 392px; top: 155px; }
  .letterhead .contact-list { left: 464px; top: 63px; }

  .recipient-label { position: absolute; left: 66px; top: 184px; font-size: 14px; color: var(--text-soft); }

  .footer-contacts { position: absolute; left: 64px; top: 673px; list-style: none; }
  .footer-contacts li { display: flex; align-items: center; gap: 14px; height: 32px; margin-bottom: 9px; font-size: 11px; line-height: 14px; color: var(--text-grey); }
  .icon-tile { width: 32px; height: 32px; border-radius: 4px; background: var(--brand-blue); display: flex; align-items: center; justify-content: center; flex-shrink: 0; }
  .icon-tile svg { width: 20px; height: 20px; fill: none; stroke: #fff; stroke-width: 1.3; stroke-linejoin: round; stroke-linecap: round; }
</style>
</head>
<body>

<section class="sheet business-card">
  <div class="wordmark"><span class="wordmark-square"></span>Framewell Group</div>
  <p class="holder-name">Dorian Pell</p>
  <p class="holder-role">owner</p>
  <span class="accent-rule"></span>
  <p class="postal-address">PO BOX 50872 Northgate Po<br>Calder, AB T5X-K4</p>
  <ul class="contact-list">
    <li><svg viewBox="0 0 10 10"><path d="M2 0.5 L4 2.8 L3 4 Q4.5 6 6 7 L7.2 6 L9.5 8 L8 9.5 Q3.5 9 0.5 2 Z"/></svg>+1 (0) 555 204 718</li>
    <li><svg viewBox="0 0 10 10"><rect x="0" y="1.5" width="10" height="7"/></svg>info@framewell.ca</li>
    <li><svg viewBox="0 0 10 10"><circle cx="5" cy="5" r="5"/></svg>www.framewell.ca</li>
  </ul>
</section>

<section class="sheet letterhead">
  <div class="wordmark"><span class="wordmark-square"></span>Framewell Group</div>
  <ul class="contact-list">
    <li><svg viewBox="0 0 10 10"><path d="M2 0.5 L4 2.8 L3 4 Q4.5 6 6 7 L7.2 6 L9.5 8 L8 9.5 Q3.5 9 0.5 2 Z"/></svg>+1 (0) 555 204 718</li>
    <li><svg viewBox="0 0 10 10"><rect x="0" y="1.5" width="10" height="7"/></svg>info@framewell.ca</li>
    <li><svg viewBox="0 0 10 10"><circle cx="5" cy="5" r="5"/></svg>www.framewell.ca</li>
  </ul>

  <p class="recipient-label">To...</p>
  <span class="accent-rule"></span>

  <ul class="footer-contacts">
    <li>
      <span class="icon-tile"><svg viewBox="0 0 20 20"><path d="M2 10 L10 3 L18 10 M4.5 8 V17 H15.5 V8"/></svg></span>
      <span>14 Oak Lane<br>Harlow Ridge 2045</span>
    </li>
    <li>
      <span class="icon-tile"><svg viewBox="0 0 20 20"><rect x="2" y="5" width="16" height="11"/><path d="M2 5 L10 11.5 L18 5"/></svg></span>
      <span>office@framewellgroup.com</span>
    </li>
    <li>
      <span class="icon-tile"><svg viewBox="0 0 20 20"><path d="M5 2.5 L8 6 L6.5 8 Q8.5 11.5 12 13.5 L14 12 L17.5 15 L15.5 17.5 Q7 16.5 2.5 5 Z"/><path d="M12 3 A5 5 0 0 1 17 8 M12 6 A2 2 0 0 1 14 8"/></svg></span>
      <span>071 555 0284</span>
    </li>
  </ul>
</section>

</body>
</html>
```